QT Bridgeway Business Card design

I need a business card design based on the logo you did for me.

Some where it should say "Online & Social Media Marketing"

I would like to see how you would do a double sided design. Although I may go with one side and have the other side just a sold color.

Industry/Entity Type

Business

```html
<!DOCTYPE html>
<html lang="en">
<head>
<meta charset="utf-8">
<title>QT Bridgeway Business Card</title>
<link href="https://fonts.googleapis.com/css2?family=Libre+Baskerville&display=swap" rel="stylesheet">
<style>
  :root {
    --backdrop: #e4e4e4;
    --card-white: #ffffff;
    --ink: #111111;
    --olive: #948a55;
    --rule: #000000;
    --back-black: #000000;
    --icon-grey: #dcdcdc;
    --serif: "Libre Baskerville", "Baskerville", Georgia, serif;
  }
  * { margin: 0; padding: 0; box-sizing: border-box; }
  html, body {
    width: 1200px; height: 1000px; overflow: hidden;
    background: var(--backdrop);
    font-family: var(--serif);
    color: var(--ink);
  }
  .card {
    position: absolute; left: 188px; width: 827px; height: 483px;
    box-shadow: 6px 6px 10px rgba(0,0,0,0.45);
    overflow: hidden;
  }
  .card-front { top: 9px; background: var(--card-white); }
  .card-back { top: 505px; background: var(--back-black); }

  .brand-mark {
    position: absolute; left: 34px; top: 36px;
    display: flex; align-items: center; gap: 10px;
  }
  .brand-name {
    font-size: 25px; line-height: 1.2; color: var(--olive);
    letter-spacing: 0.5px;
  }
  .brand-dot { width: 12px; height: 12px; border-radius: 50%; background: var(--olive); }

  .social-list { position: absolute; right: 33px; top: 23px; list-style: none; }
  .social-item {
    display: flex; align-items: center; height: 43px;
    font-size: 19.5px;
  }
  .social-icon {
    width: 30px; height: 30px; border-radius: 50%;
    background: var(--icon-grey);
    box-shadow: 0 3px 4px rgba(0,0,0,0.3);
    margin-right: 15px;
  }

  .identity { position: absolute; left: 0; width: 100%; top: 182px; text-align: center; }
  .person-name { font-size: 31px; font-weight: 400; letter-spacing: 1px; }
  .person-role { font-size: 17px; margin-top: 8px; }
  .website {
    position: absolute; left: 0; width: 100%; top: 332px;
    text-align: center; font-size: 19px;
  }

  .contact-band {
    position: absolute; left: 0; top: 366px; width: 100%; height: 117px;
    background: var(--olive); border-top: 5px solid var(--rule);
  }
  .contact-lines { position: absolute; left: 36px; top: 22px; font-size: 18px; }
  .contact-lines p { height: 38px; }
  .contact-label { color: var(--card-white); margin-right: 10px; }
  .address {
    position: absolute; right: 33px; top: 22px;
    text-align: right; font-size: 20px;
  }
  .address p { height: 39px; }

  .back-mark {
    position: absolute; left: 0; top: 0; width: 100%; height: 100%;
    display: flex; align-items: center; justify-content: center; gap: 26px;
  }
  .back-name {
    color: var(--olive); font-size: 76px; line-height: 1.05;
    text-align: left; letter-spacing: 2px;
  }
  .back-dot { width: 40px; height: 40px; border-radius: 50%; background: var(--olive); margin-top: -90px; }
</style>
</head>
<body>
  <section class="card card-front">
    <div class="brand-mark">
      <span class="brand-name">QT<br>BRIDGEWAY</span>
      <span class="brand-dot"></span>
    </div>
    <ul class="social-list">
      <li class="social-item"><span class="social-icon"></span>profile name</li>
      <li class="social-item"><span class="social-icon"></span>profile name</li>
    </ul>
    <div class="identity">
      <h1 class="person-name">NORA ELLINGWOOD</h1>
      <p class="person-role">Online &amp; Social Media Marketing</p>
    </div>
    <p class="website">www.QTBRIDGEWAY.com</p>
    <div class="contact-band">
      <div class="contact-lines">
        <p><span class="contact-label">p</span>555.204.6318</p>
        <p><span class="contact-label">e</span>email@email.com</p>
      </div>
      <div class="address">
        <p>42 Harborview Lane</p>
        <p>Easton Bay, MA 02990</p>
      </div>
    </div>
  </section>

  <section class="card card-back">
    <div class="back-mark">
      <div class="back-name">QT<br>BRIDGEWAY</div>
      <span class="back-dot"></span>
    </div>
  </section>
</body>
</html>
```